Wordpress Design Project for Employee Communications Site

We need a Wordpress design for a company that strategizes on and produces materials for employee communications. Improving employee communications at all levels of an organization can help improve overall company performance and results. The site needs to look very clean and professional; we're not afraid of white space. We like the functionality that Wordpress provides; however, we only want one "true" blog page; the other pages should give the impression of a more "static" web site - particularly the home page. I have a logo that I can provide.

I have added these comments to the discussion page:
Great question - thank you for asking it. I’ve done more research

I like the very clean and monochromatic looks to many of these. I don’t have to have monochromatic, but I do like minimal colors. Simple, clean, organized. The home page should “fit” almost entirely without scrolling. I do like fat footers that you can scroll down to. I don’t want a colored background, but any that I’ve chosen with colored backgrounds could be switched to a white background.

http://www.moravelkinst.com/
http://pondrix.com/
http://v1.belmarquist.com/
http://howtheotter.com/
http://stayingnimble.com/
http://www.interiors.pelmun.co.uk/
http://brixalumnihub.com/

These last two are more corporate sites. The first one is from a well-respected consultant in my area who does a lot of what I do. And I think Harwick does a nice job with their site. So, I want to marry the look I like with getting the content job done.

http://www.messagefuelworks.com/
http://www.harwick.com/view/en_US/us/index.htm

Target Market(s)

Target market is mid- to large-sized companies. More than 500 employees.

Industry/Entity Type

Communications

Requirements
Must have
• Need an impactful home page. There should be a "blog" page; contact us; services; about. For starters, at least. I want fonts to be very readable - that is, either quite dark gray or black.
Nice to have
• I am loathe to include a picture of myself, but I do want some images that say, "professional" and "expert" in communications.
Should not have
• I don't want a hits counter :) (I know no one would do that!).

```html
<!DOCTYPE html>
<html lang="en">
<head>
<meta charset="utf-8">
<title>Meridian Workplace Communications</title>
<link rel="stylesheet" href="https://fonts.googleapis.com/css2?family=Droid+Serif:ital,wght@1,700&family=Ubuntu:wght@300;400;500&family=Oswald:wght@500&display=swap">
<style>
:root{
  --blue:#1a9fd6;
  --blue-dark:#0d86bd;
  --green:#8dc21f;
  --ink:#2a2a2a;
  --body:#3a3a3a;
  --muted:#777;
  --line:#d9d9d9;
  --panel:#2b2b2b;
  --paper:#ffffff;
  --mist:#eef0f2;
}
*{box-sizing:border-box;margin:0;padding:0}
html,body{width:780px;height:1200px;overflow:hidden}
body{position:relative;background:var(--paper);font-family:"Ubuntu",Arial,sans-serif;color:var(--body)}
.abs{position:absolute}
.hero-band{left:0;top:117px;width:780px;height:272px;background:linear-gradient(#f7f8f9,#eceef0)}
.footer-band{left:0;top:1110px;width:780px;height:90px;background:linear-gradient(var(--blue),var(--blue-dark))}
.page{left:109px;top:0;width:562px;height:1162px;background:var(--paper);box-shadow:0 0 6px rgba(0,0,0,.18)}
.page-top{left:109px;top:0;width:562px;height:117px;background:var(--paper)}
/* header */
.brand{left:131px;top:14px;display:flex;align-items:center;gap:10px}
.brand-dot{width:46px;height:46px;border-radius:50%;background:var(--blue)}
.brand-name{font-family:"Ubuntu",sans-serif;font-weight:300;font-size:21px;line-height:23px;color:var(--green)}
.search{left:518px;top:47px;width:140px;height:17px;border:1px solid #cfcfcf;border-radius:3px;background:#fafafa;font-size:8px;color:#999;padding:3px 5px}
.search svg{position:absolute;right:4px;top:2px}
.nav{left:102px;top:81px;width:576px;height:33px;background:linear-gradient(#29b3e8,var(--blue));border-radius:4px;box-shadow:0 2px 3px rgba(0,0,0,.2)}
.nav a{position:absolute;top:11px;font-size:11.5px;color:#fff;text-decoration:none}
.nav .current{top:7px;height:26px;padding:6px 9px 0;background:var(--paper);color:#333;border-radius:3px 3px 0 0}
/* hero */
.hero-photo{left:109px;top:117px;width:562px;height:283px;background:linear-gradient(90deg,#d8dbde 0%,#f3f4f5 45%,#e4e2df 70%,#c9c6c1 85%,#eceeef 100%)}
.hero-caption{left:119px;top:183px;width:297px;height:146px;background:rgba(32,32,32,.88);padding:17px 14px}
.hero-caption::after{content:"";position:absolute;right:-10px;top:58px;border:10px solid transparent;border-left-color:rgba(32,32,32,.88);border-right:0}
.hero-title{font-family:"Droid Serif",Georgia,serif;font-style:italic;font-weight:700;font-size:13px;color:var(--green);margin-bottom:9px}
.hero-text{font-size:10.5px;line-height:14.5px;color:#d8d8d8;text-align:justify}
.btn-start{left:294px;top:299px;width:94px;height:21px;background:var(--blue);border-radius:4px;font-family:"Oswald",sans-serif;font-size:12px;color:#fff;text-align:center;line-height:21px}
.dots span{position:absolute;top:394px;width:9px;height:9px;border-radius:50%;background:#e4e6e8;box-shadow:inset 0 1px 2px rgba(0,0,0,.2)}
.dots .on{background:var(--blue)}
/* content */
.section-title{font-family:"Droid Serif",Georgia,serif;font-style:italic;font-weight:700;font-size:13px;color:var(--green)}
.copy{font-size:7.4px;line-height:14.4px;color:var(--body);text-align:justify}
.btn-more{left:408px;top:534px;width:58px;height:18px;background:var(--blue);border-radius:4px;font-family:"Oswald",sans-serif;font-size:11px;color:#fff;text-align:center;line-height:18px}
.date{width:31px;height:31px;border:1px solid #ccc;border-radius:4px;background:#fff;text-align:center;box-shadow:0 1px 2px rgba(0,0,0,.15)}
.date b{display:block;font-size:12px;color:var(--green);line-height:14px;margin-top:3px}
.date small{display:block;font-size:7px;color:#555}
.post-title{font-size:10.5px;color:var(--ink);font-weight:500}
.post-meta{font-size:7px;color:#555}
.post-meta em{font-style:normal;color:var(--blue)}
.post-frame{border:1px solid #e3e3e3;padding:4px;background:#fff}
.post-img{width:100%;height:100%}
.share{width:40px;height:30px;background:linear-gradient(#555,#2a2a2a);border-radius:4px;color:#fff;font-size:7px;font-weight:500;text-align:center;padding-top:3px}
.share i{display:block;margin:3px 3px 0;background:#fff;color:#333;border-radius:2px;font-style:normal;font-size:7px;line-height:10px}
.social-row{display:flex;gap:4px;font-size:6.5px;color:#444;align-items:center}
.chip{border:1px solid #c8c8c8;border-radius:2px;padding:1px 4px;background:#f6f6f6}
.chip.blue{background:#4a8fd8;color:#fff;border-color:#3a74b3}
.chip.light{background:#e8f3fb;color:#3a74b3}
.pager{left:253px;top:1127px;display:flex;gap:5px}
.pager span{height:14px;min-width:15px;padding:0 4px;background:linear-gradient(#f5f5f5,#d6d6d6);border:1px solid #bbb;border-radius:3px;font-size:6.5px;line-height:12px;text-align:center;color:#333}
.pager .cur{background:#9a9a9a;color:#fff}
.pager .wide{padding:0 10px}
/* sidebar */
.side-head{left:494px;width:184px;height:34px;background:linear-gradient(#29b3e8,var(--blue));border-radius:4px 4px 0 4px;font-family:"Droid Serif",Georgia,serif;font-style:italic;font-weight:700;font-size:12.5px;color:#fff;text-align:right;padding:10px 12px 0 0}
.side-head .tag{position:absolute;left:10px;top:12px;font-family:"Ubuntu",sans-serif;font-style:normal;font-weight:400;font-size:7px}
.side-head .box{position:absolute;left:7px;top:8px;width:17px;height:17px;background:#fff;border-radius:2px}
.news-day{width:30px;height:30px;border-radius:50%;background:var(--blue);border:2px solid #dff1fa;color:#fff;font-size:12px;font-weight:500;text-align:center;line-height:26px}
.news-text{width:131px;font-size:7.4px;line-height:9px;color:var(--ink);text-align:justify}
.news-date{font-size:7px;color:var(--blue);font-weight:500}
.fans{font-size:7px;color:#444;line-height:9px}
.like-btn{left:604px;top:655px;width:55px;height:14px;border:1px solid #c9d5e6;background:#eef3fa;border-radius:2px;font-size:6.5px;color:#3b5b93;padding:2px 4px}
.fan{width:27px}
.fan-pic{width:27px;height:27px;border:1px solid #ccc}
.fan-name{font-size:4.5px;color:#666;text-align:center;margin-top:2px}
.services{left:498px;top:820px;width:172px;list-style:none}
.services li{height:21.5px;border-bottom:1px dashed #bbb;font-size:10px;color:#333;padding:4px 0 0 20px;position:relative}
.services li::before{content:"";position:absolute;left:8px;top:8px;border:3.5px solid transparent;border-left:4px solid #999;border-right:0}
.follow span{position:absolute;top:998px;width:24px;height:24px;border:1px solid #ccc;border-radius:3px;background:linear-gradient(#fff,#ececec);box-shadow:0 1px 2px rgba(0,0,0,.15)}
.follow span i{position:absolute;left:7px;top:7px;width:8px;height:8px;background:#444;border-radius:50%}
.follow span i.sq{border-radius:1px}
/* footer */
.footer-links{left:122px;top:1177px;font-size:8px;color:#fff}
.footer-links span{margin:0 8px}
.copyright{left:475px;top:1176px;font-size:7.5px;color:#fff}
</style>
</head>
<body>
<div class="abs hero-band"></div>
<div class="abs footer-band"></div>
<div class="abs page"></div>

<header>
  <div class="abs brand">
    <span class="brand-dot"></span>
    <span class="brand-name">Meridian Workplace<br>Communications</span>
  </div>
  <div class="abs search">Search
    <svg width="12" height="12" viewBox="0 0 12 12"><circle cx="5" cy="5" r="3.6" fill="none" stroke="#888" stroke-width="1.6"/><line x1="7.6" y1="7.6" x2="11" y2="11" stroke="#888" stroke-width="2"/></svg>
  </div>
  <nav class="abs nav">
    <a class="current" style="left:132px">Home</a>
    <a style="left:198px">About us</a>
    <a style="left:268px">Services</a>
    <a style="left:335px">Blog</a>
    <a style="left:385px">Contact us</a>
  </nav>
</header>

<section class="hero">
  <div class="abs hero-photo" role="img" aria-label="Photo of business people walking with a smiling professional woman holding a folder"></div>
  <div class="abs hero-caption">
    <h1 class="hero-title">Meridian Workplace Communications</h1>
    <p class="hero-text">Sed ut perspiciatis unde omnis iste natus error sit voluptatem accusantium doloremque laudantium, totam rem aperiam, eaque ipsa quae ab illo inventore veritatis Nemo enim ipsam voluptatem quia voluptas sit aspernatur aut odit</p>
  </div>
  <div class="abs btn-start">GET STARTED</div>
  <div class="dots"><span style="left:367px"></span><span style="left:386px"></span><span class="on" style="left:405px"></span></div>
</section>

<main>
  <h2 class="abs section-title" style="left:117px;top:418px">Welcome to MWC</h2>
  <p class="abs copy" style="left:121px;top:445px;width:349px">On the other hand, we denounce with righteous indignation and dislike men who are so beguiled and demoralized by the charms of pleasure of the moment, so blinded by desire, that they cannot foresee the pain and trouble that are bound to ensue; and equal blame belongs to those who fail in their duty through weakness of will, which is the same as saying through shrinking from toil and pain. These cases are perfectly simple and easy to distinguish. In a free hour, when our power of choice is untrammelled and when nothing prevents our being able to do what we like best, every pleasure is to be welcomed and every pain avoided.</p>
  <div class="abs btn-more">MORE</div>

  <h2 class="abs section-title" style="left:118px;top:555px">Our Recent Blog Posts</h2>

  <article>
    <div class="abs date" style="left:118px;top:579px"><b>06</b><small>Aug</small></div>
    <h3 class="abs post-title" style="left:156px;top:581px">I Must explain to you how all</h3>
    <p class="abs post-meta" style="left:158px;top:598px">Posted by <em>admin</em></p>
    <p class="abs post-meta" style="left:302px;top:598px">Posted in <em>Modern webdesign Programming</em></p>
    <div class="abs post-frame" style="left:121px;top:619px;width:346px;height:132px">
      <div class="post-img" role="img" aria-label="Illustration of a computer monitor and a tablet showing technical screens" style="background:linear-gradient(90deg,#e9ecef,#f6f7f8 30%,#d9503a 45%,#c73b2a 55%,#2aa3e0 65%,#f2f3f4 80%,#e5e7e9)"></div>
    </div>
    <div class="abs share" style="left:125px;top:757px">SHARE<i>0</i></div>
    <p class="abs copy" style="left:174px;top:753px;width:288px">On the other hand, we denounce with righteous indignation and dislike men who are so beguiled and demoralized by the charms of pleasure of the moment, so blinded by desire, that they cannot foresee the pain and trouble that are bound to ensue; and equal blame belongs to those who fail in their duty through weakness of will, which is the same as saying through shrinking from toil and pain. These cases are perfectly simple and easy to distinguish.</p>
    <div class="abs social-row" style="left:285px;top:830px"><span class="chip">129 people</span><span class="chip blue">Hum</span><span class="chip">43</span><span class="chip light">Chirp</span><span class="chip">932</span></div>
  </article>

  <article>
    <div class="abs date" style="left:118px;top:851px"><b>06</b><small>Aug</small></div>
    <h3 class="abs post-title" style="left:156px;top:853px">I Must explain to you how all</h3>
    <p class="abs post-meta" style="left:158px;top:870px">Posted by <em>admin</em></p>
    <p class="abs post-meta" style="left:302px;top:870px">Posted in <em>Modern webdesign Programming</em></p>
    <div class="abs post-frame" style="left:121px;top:891px;width:346px;height:129px">
      <div class="post-img" role="img" aria-label="Photo of a smiling team of five business professionals" style="background:linear-gradient(90deg,#d7c3b0,#b08a6a 30%,#e8d8c4 50%,#8a6a55 75%,#d9cbbd)"></div>
    </div>
    <div class="abs share" style="left:125px;top:1029px">SHARE<i>0</i></div>
    <p class="abs copy" style="left:174px;top:1024px;width:288px">On the other hand, we denounce with righteous indignation and dislike men who are so beguiled and demoralized by the charms of pleasure of the moment, so blinded by desire, that they cannot foresee the pain and trouble that are bound to ensue; and equal blame belongs to those who fail in their duty through weakness of will, which is the same as saying through shrinking from toil and pain. These cases are perfectly simple and easy to distinguish.</p>
    <div class="abs social-row" style="left:282px;top:1105px"><span class="chip">129 people</span><span class="chip blue">Hum</span><span class="chip">43</span><span class="chip light">Chirp</span><span class="chip">932</span></div>
  </article>

  <div class="abs pager"><span class="wide">‹ PREV</span><span>1</span><span>2</span><span>3</span><span class="cur">4</span><span>5</span><span>…</span><span>21</span><span class="wide">NEXT ›</span></div>
</main>

<aside>
  <div class="abs side-head" style="top:406px"><span class="tag">» MORE</span>Latest News</div>
  <div class="abs news-day" style="left:499px;top:444px">24</div>
  <p class="abs news-text" style="left:533px;top:446px">Sed ut perspiciatis unde omnis iste natus error sit voluptatem accusantium doloremque laudantium,</p>
  <p class="abs news-date" style="left:624px;top:474px">Jun-2012</p>
  <div class="abs news-day" style="left:499px;top:492px">24</div>
  <p class="abs news-text" style="left:533px;top:494px">Sed ut perspiciatis unde omnis iste natus error sit voluptatem accusantium doloremque laudantium,</p>
  <p class="abs news-date" style="left:624px;top:522px">Jun-2012</p>
  <div class="abs news-day" style="left:499px;top:538px">24</div>
  <p class="abs news-text" style="left:533px;top:540px">Sed ut perspiciatis unde omnis iste natus error sit voluptatem accusantium doloremque laudantium,</p>
  <p class="abs news-date" style="left:624px;top:568px">Jun-2012</p>

  <div class="abs side-head" style="top:593px"><span class="box"></span>circlebook likes</div>
  <p class="abs fans" style="left:502px;top:632px;width:150px">Like our page and win a bundle of 150 files collection of our best graphics?</p>
  <svg class="abs" style="left:620px;top:645px" width="12" height="9" viewBox="0 0 12 9"><path d="M1 1 H9 V7 M6 4 L9 7 L11 4" fill="none" stroke="#333" stroke-width="1.2"/></svg>
  <p class="abs fans" style="left:504px;top:659px">347 Peple like <b>MWC</b></p>
  <div class="abs like-btn">Like</div>
  <div class="abs fan" style="left:499px;top:679px"><div class="fan-pic" role="img" aria-label="Fan profile photo" style="background:#b9a6a0"></div><p class="fan-name">Nora</p></div>
  <div class="abs fan" style="left:533px;top:679px"><div class="fan-pic" role="img" aria-label="Fan profile photo" style="background:#c98a5e"></div><p class="fan-name">Stevo</p></div>
  <div class="abs fan" style="left:567px;top:679px"><div class="fan-pic" role="img" aria-label="Fan profile photo" style="background:#6f7d4a"></div><p class="fan-name">Ren</p></div>
  <div class="abs fan" style="left:601px;top:679px"><div class="fan-pic" role="img" aria-label="Fan profile picture" style="background:#e6dede"></div><p class="fan-name">Marten</p></div>
  <div class="abs fan" style="left:636px;top:679px"><div class="fan-pic" role="img" aria-label="Fan profile picture" style="background:#dfe9a8"></div><p class="fan-name">Malia</p></div>
  <div class="abs fan" style="left:499px;top:721px"><div class="fan-pic" role="img" aria-label="Fan profile photo" style="background:#3a3a3a"></div><p class="fan-name">Kaspar</p></div>
  <div class="abs fan" style="left:533px;top:721px"><div class="fan-pic" role="img" aria-label="Fan profile photo" style="background:#8c9aa6"></div><p class="fan-name">Kalin</p></div>
  <div class="abs fan" style="left:567px;top:721px"><div class="fan-pic" role="img" aria-label="Fan profile picture" style="background:#e8e8e8"></div><p class="fan-name">Matilde</p></div>
  <div class="abs fan" style="left:601px;top:721px"><div class="fan-pic" role="img" aria-label="Fan profile photo" style="background:#7d7d7d"></div><p class="fan-name">Sandor</p></div>
  <div class="abs fan" style="left:636px;top:721px"><div class="fan-pic" role="img" aria-label="Fan profile picture" style="background:#c3dcc6"></div><p class="fan-name">Milo</p></div>
  <div class="abs" style="left:494px;top:768px;width:184px;height:3px;background:#ececec"></div>

  <div class="abs side-head" style="top:778px">Our Services</div>
  <ul class="abs services">
    <li>Etiam ultrices velit</li>
    <li>Donec condimentum</li>
    <li>Aenean</li>
    <li>Aliquam vehi</li>
    <li>Proin ut</li>
  </ul>

  <div class="abs side-head" style="top:947px">Follow Us</div>
  <div class="follow">
    <span style="left:516px"><i class="sq"></i></span>
    <span style="left:552px"><i></i></span>
    <span style="left:587px"><i class="sq"></i></span>
    <span style="left:622px"><i></i></span>
  </div>
</aside>

<footer>
  <p class="abs footer-links">Home<span>|</span>About us<span>|</span>Services<span>|</span>Blog<span>|</span>Contact us</p>
  <p class="abs copyright">© 2012. www.meridianworkplacecomms</p>
</footer>
</body>
</html>
```